Website design for Cloud Scheduling Company

We have a design build that is based on a corporate template. the structure and content is there but the design does not match the 'feel' of what we are going for from a design perspective.
http://plumvexo.com/demo/fen/

please follow this structure for the site layout but add new ideas also.

Scheduling is boring and typically a serious topic, with our new logo we are looking to bring a quirky, fun feeling to what our site does.

It is a powerful scheduling platform that is used mainly in Volunteer environments and we want our brand to reflect this.

A lot of sites use images of real people in photographs but i would like to see us use more vector graphics and illustrations in the design so it is a bit more exciting.

The homepage should have a large screen capture of the app on different devices (large monitor, tablet, and smartphone) which is pretty standard for this type of website.i have attached a jpeg where you can get images from as well as the logo so you can get a sense of the look and feel.

this is what I envision being the image in the main banner as it showcases the application https://www.trindlesk.ca/search?q=responsive&biw=1920&bih=920&source=lnms&tbm=isch&sa=X&ved=0ahUKEwiAlqahjv_KAhXrlIMKHToqB5oQ_AUIBigB#imgrc=a75LOlLuwcKyqM%3A

Again, what I need for this project is a design for the site at http://plumvexo.com/demo/fen/. it is already coded but i need a netter design. focus on homepage, pricing page and a general subpage please.

Target Market(s)

Volunteer organization Administrators

Industry/Entity Type

It Company

Number of Pages Required

3 page

Font styles to use
Sans Serif

Colors
0355a3
f37122

Requirements
Nice to have
• use graphics instead of photographs. you can include some photos but i want the look and feel to be consistent with the playfulness of the logo so the site isnt too serious. The site still has to be professional.

```html
<!DOCTYPE html>
<html lang="en">
<head>
<meta charset="utf-8">
<title>Fenrota – Pricing</title>
<link href="https://fonts.googleapis.com/css2?family=Raleway:wght@500;600;700&family=Jost:wght@400;500&family=Bree+Serif&family=Lato:wght@400;700;900&display=swap" rel="stylesheet">
<style>
:root{
  --orange:#f08a24;
  --orange-light:#f8ab3f;
  --navy:#1b5682;
  --navy-light:#2c78a8;
  --footer:#1d5384;
  --bottom:#2d3039;
  --ink:#333;
  --muted:#555;
  --page:#f1f1f1;
  --line:#dcdcdc;
}
*{box-sizing:border-box;margin:0;padding:0}
html,body{width:965px;height:1200px;overflow:hidden}
body{background:var(--page);font-family:'Jost',sans-serif;color:var(--ink);position:relative}
.topline{height:3px;background:var(--orange)}
.header{height:64px;background:#fff;position:relative}
.brand{position:absolute;left:132px;top:16px;display:flex;align-items:center;gap:8px}
.brand-dot{width:26px;height:26px;border-radius:50%;background:var(--navy)}
.brand-name{font-family:'Raleway',sans-serif;font-weight:700;font-size:25px;color:var(--orange)}
.nav{position:absolute;right:132px;top:20px;display:flex;align-items:center;gap:22px;font-size:12px;color:#555}
.nav .caret::after{content:"";display:inline-block;margin-left:3px;border:3px solid transparent;border-top-color:#555;vertical-align:middle}
.btn-start{border:1px solid var(--orange);color:var(--orange);border-radius:3px;padding:5px 18px;font-size:13px}
.hero{position:relative;height:235px;background:linear-gradient(90deg,#3c3630 0%,#6e5a48 45%,#a08470 70%,#d8cfc6 100%)}
.hero-copy{position:absolute;left:132px;top:64px;color:#fff}
.hero h1{font-family:'Raleway',sans-serif;font-weight:600;font-size:30px;text-shadow:0 1px 3px rgba(0,0,0,.4)}
.hero .tag{display:inline-block;margin-top:8px;background:var(--navy);border:1px solid #8fb3d0;border-radius:2px;padding:6px 10px;font-family:'Raleway',sans-serif;font-weight:600;font-size:13px}
.hero p{margin-top:9px;font-family:'Raleway',sans-serif;font-weight:600;font-size:11px;line-height:16px}
.crumbs{height:29px;background:linear-gradient(#dedede,#eaeaea);font-family:'Lato',sans-serif;font-size:10px;padding:9px 0 0 132px}
.crumbs .sep{margin:0 6px;color:#777}
.crumbs .here{color:#3b7ab0}
.pricing{text-align:center;padding-top:33px}
.pricing h2{font-family:'Raleway',sans-serif;font-weight:600;font-size:25px;color:var(--navy)}
.divider{position:relative;margin:11px auto 0;width:705px;height:20px}
.divider::before{content:"";position:absolute;left:0;right:0;top:8px;border-top:1px solid var(--line)}
.divider i{position:relative;display:block;margin:0 auto;width:16px;height:16px;border-radius:50%;background:var(--navy)}
.pricing h3{font-family:'Bree Serif',serif;font-weight:400;font-size:13px;margin-top:5px;color:#222}
.pricing .lead{font-size:11px;margin-top:7px;color:#444}
.plans{display:flex;gap:26px;justify-content:center;margin-top:14px}
.plan{width:218px;height:407px;background:#fff;border:1px solid #e2e2e2;border-radius:0 0 4px 4px;position:relative}
.plan-head{position:relative;height:86px}
.plan-head svg{position:absolute;left:-1px;top:-1px}
.plan-head span{position:absolute;left:0;right:0;top:24px;font-family:'Raleway',sans-serif;font-weight:600;font-size:24px;color:#fff}
.price{font-family:'Bree Serif',serif;font-size:18px;color:var(--orange);margin-top:14px}
.plan.featured .price{color:var(--navy)}
.plan .divider{width:170px;margin-top:6px}
.plan .divider i{width:13px;height:13px}
.features{list-style:none;font-size:10.5px;color:#444;margin-top:6px}
.features li{height:21.7px;line-height:21.7px}
.features li.lead-item{font-family:'Bree Serif',serif;font-size:12px;color:#222}
.trial{display:block;margin:10px auto 0;width:164px;height:28px;line-height:28px;background:var(--navy);color:#fff;font-family:'Raleway',sans-serif;font-weight:600;font-size:11px;border:1px solid #123e60}
.plan.featured .trial{background:var(--orange);border-color:#d8731a}
.note{font-family:'Lato',sans-serif;font-size:8.5px;color:#444;margin-top:11px}
.note b{color:var(--orange);font-weight:900;margin-left:4px}
.newsletter{position:absolute;left:0;top:950px;width:965px;height:52px;background:var(--orange);display:flex;align-items:center;padding-left:132px}
.mail-ring{width:36px;height:36px;border:2px solid #fff;border-radius:50%;display:flex;align-items:center;justify-content:center}
.newsletter h4{font-family:'Raleway',sans-serif;font-weight:500;font-size:19px;color:#fff;margin-left:9px;width:230px}
.email{width:259px;height:27px;background:#fff;border:1px solid #e5e5e5;font-family:'Lato',sans-serif;font-size:9px;color:#888;padding:8px 7px}
.subscribe{margin-left:10px;width:132px;height:27px;background:var(--bottom);color:#fff;font-family:'Raleway',sans-serif;font-weight:700;font-size:13px;letter-spacing:.5px;text-align:center;line-height:27px}
.footer{position:absolute;left:0;top:1002px;width:965px;height:160px;background:var(--footer);color:#fff}
.footer h5{font-family:'Raleway',sans-serif;font-weight:600;font-size:17px}
.quick{position:absolute;left:131px;top:18px}
.quick ul{list-style:none;margin-top:8px;font-size:10px;line-height:17.4px;color:#dce6f0}
.contact{position:absolute;left:314px;top:18px;width:210px}
.map{position:absolute;left:6px;top:22px;width:210px;height:100px;background:rgba(255,255,255,.06);border-radius:40px}
.contact .row{position:relative;display:flex;gap:10px;align-items:flex-start;font-size:10px;margin-top:8px}
.contact .row:first-of-type{margin-top:10px}
.contact .name{font-family:'Bree Serif',serif;color:var(--orange);font-size:9.5px}
.contact .ic{width:14px;flex:none}
.tweets{position:absolute;left:545px;top:18px;width:290px;height:124px;background:#fff;border-radius:3px;color:#333}
.tweets-head{display:flex;justify-content:space-between;align-items:center;padding:6px 8px;border-bottom:1px solid #e5e5e5;font-family:'Lato',sans-serif;font-weight:700;font-size:12px;height:25px}
.follow{border:1px solid #ccc;border-radius:2px;background:#f4f4f4;font-size:8px;padding:2px 6px}
.tweet{display:flex;gap:7px;padding:6px 6px;border-bottom:1px solid #e5e5e5;font-family:'Lato',sans-serif;font-size:7.5px;line-height:11px;height:50px}
.tweet:last-child{border:0}
.avatar{width:31px;height:31px;border:1px solid #ddd;background:#e8eef4;flex:none}
.tweet .meta{display:flex;justify-content:space-between;font-weight:700;color:#333}
.tweet .meta a{color:#29a3e0;font-weight:400;text-decoration:none}
.tweet .meta time{font-weight:400;color:#777}
.bottombar{position:absolute;left:0;top:1162px;width:965px;height:38px;background:var(--bottom);color:#fff;font-size:10px;padding:0 131px;display:flex;justify-content:space-between;align-items:center}
.social{display:flex;gap:9px}
.social i{width:19px;height:19px;border-radius:50%;background:#d8d8d8;display:block}
.social i.active{background:var(--orange)}
</style>
</head>
<body>
<div class="topline"></div>
<header class="header">
  <div class="brand"><span class="brand-dot"></span><span class="brand-name">fenrota.com</span></div>
  <nav class="nav">
    <span>Home</span><span class="caret">Pages</span><span class="caret">Features</span><span class="caret">Portfolio</span><span>Admin Theme</span>
    <span class="btn-start">Start Now</span>
  </nav>
</header>
<section class="hero" role="img" aria-label="Photo of a smiling woman in a bright office">
  <div class="hero-copy">
    <h1>Free yourself from</h1>
    <div class="tag">Mundane Repetitive Scheduling</div>
    <p>FENROTA makes the Scheduling process<br>simple for you and even simpler for your Volunteers</p>
  </div>
</section>
<div class="crumbs">Home<span class="sep">»</span><span class="here">Pricing</span></div>

<main class="pricing">
  <h2>Pricing</h2>
  <div class="divider"><i></i></div>
  <h3>All Plans Include a Free 30Day Trial</h3>
  <p class="lead">Lorem ipsum dolor sit amet, consectetuer adipiscing elit, sed diam nonummy nibh euismod tincidunt ut laoreet.</p>

  <div class="plans">
    <article class="plan">
      <div class="plan-head">
        <svg width="218" height="88" viewBox="0 0 218 88"><defs><linearGradient id="og" x1="0" y1="0" x2="0" y2="1"><stop offset="0" stop-color="#f08a24"/><stop offset="1" stop-color="#f8ab3f"/></linearGradient></defs><polygon points="0,72 109,80 218,72 218,78 109,86 0,78" fill="#e3e3e3"/><polygon points="0,0 218,0 218,70 109,82 0,70" fill="url(#og)"/></svg>
        <span>Deluxe</span>
      </div>
      <div class="price">$59 per user/month</div>
      <div class="divider"><i></i></div>
      <ul class="features">
        <li class="lead-item">Lorem ipsum dolor sit amet</li>
        <li>Lorem ipsum dolor sit amet</li><li>Lorem ipsum dolor sit amet, consectetuer</li>
        <li>Lorem ipsum dolor sit amet</li><li>Lorem ipsum dolor sit amet, consectetuer</li>
        <li>Lorem ipsum dolor sit amet</li><li>Lorem ipsum dolor sit amet, consectetuer</li>
        <li>Lorem ipsum dolor sit amet</li>
      </ul>
      <span class="trial">Start Your Free Trial</span>
      <p class="note">No credit card required</p>
    </article>

    <article class="plan featured">
      <div class="plan-head">
        <svg width="218" height="88" viewBox="0 0 218 88"><defs><linearGradient id="ng" x1="0" y1="0" x2="0" y2="1"><stop offset="0" stop-color="#1b5682"/><stop offset="1" stop-color="#2c78a8"/></linearGradient></defs><polygon points="0,72 109,80 218,72 218,78 109,86 0,78" fill="#e3e3e3"/><polygon points="0,0 218,0 218,70 109,82 0,70" fill="url(#ng)"/></svg>
        <span>Premium</span>
      </div>
      <div class="price">$99 per user/month</div>
      <div class="divider"><i></i></div>
      <ul class="features">
        <li class="lead-item">Lorem ipsum dolor sit amet</li>
        <li>Lorem ipsum dolor sit amet</li><li>Lorem ipsum dolor sit amet, consectetuer</li>
        <li>Lorem ipsum dolor sit amet</li><li>Lorem ipsum dolor sit amet, consectetuer</li>
        <li>Lorem ipsum dolor sit amet</li><li>Lorem ipsum dolor sit amet, consectetuer</li>
        <li>Lorem ipsum dolor sit amet</li>
      </ul>
      <span class="trial">Start Your Free Trial</span>
      <p class="note">No credit card required</p>
    </article>

    <article class="plan">
      <div class="plan-head">
        <svg width="218" height="88" viewBox="0 0 218 88"><polygon points="0,72 109,80 218,72 218,78 109,86 0,78" fill="#e3e3e3"/><polygon points="0,0 218,0 218,70 109,82 0,70" fill="url(#og)"/></svg>
        <span>Team</span>
      </div>
      <div class="price">$500 per month, 3 users</div>
      <div class="divider"><i></i></div>
      <ul class="features">
        <li class="lead-item">Lorem ipsum dolor sit amet</li>
        <li>Lorem ipsum dolor sit amet</li><li>Lorem ipsum dolor sit amet, consectetuer</li>
        <li>Lorem ipsum dolor sit amet</li><li>Lorem ipsum dolor sit amet, consectetuer</li>
        <li>Lorem ipsum dolor sit amet</li><li>Lorem ipsum dolor sit amet, consectetuer</li>
        <li>Lorem ipsum dolor sit amet</li>
      </ul>
      <span class="trial">Start Your Free Trial</span>
      <p class="note">No credit card required <b>• Request Demo</b></p>
    </article>
  </div>
</main>

<section class="newsletter">
  <div class="mail-ring"><svg width="20" height="14" viewBox="0 0 20 14"><rect x="1" y="1" width="18" height="12" fill="none" stroke="#fff" stroke-width="2"/><path d="M1 1 L10 8 L19 1" fill="none" stroke="#fff" stroke-width="2"/></svg></div>
  <h4>Sign Up For Newsletter</h4>
  <div class="email">Enter your email here</div>
  <div class="subscribe">SUBSCRIBE</div>
</section>

<footer class="footer">
  <div class="quick">
    <h5>Quick Link</h5>
    <ul><li>Home</li><li>Pages</li><li>Features</li><li>Portfolio</li><li>Admin Theme</li></ul>
  </div>
  <div class="contact">
    <div class="map" role="img" aria-label="Faint dotted world map"></div>
    <h5 style="position:relative">Contact Info</h5>
    <div class="row"><svg class="ic" width="16" height="12" viewBox="0 0 16 12"><path d="M1 11 L8 2 L15 11" fill="none" stroke="#f08a24" stroke-width="2"/></svg><div><div class="name">Fenrota</div>Lindenweg 14 80331 Marbach</div></div>
    <div class="row" style="margin-top:14px"><svg class="ic" width="12" height="12" viewBox="0 0 12 12"><path d="M2 1 L4.5 1 L5.5 4 L4 5 Q5 7.5 7 8 L8 6.5 L11 7.5 L11 10 Q11 11 9.5 11 Q1 10 1 2.5 Q1 1 2 1Z" fill="#fff"/></svg><span style="font-family:'Bree Serif',serif;font-size:9px">+49 - 55-0123 45678</span></div>
    <div class="row" style="margin-top:10px"><svg class="ic" width="12" height="9" viewBox="0 0 12 9"><rect width="12" height="9" fill="#fff"/><path d="M0 0 L6 5 L12 0" fill="none" stroke="#1d5384" stroke-width="1.2"/></svg><span style="font-size:11px">info@fenrotaeu.com</span></div>
  </div>
  <div class="tweets">
    <div class="tweets-head">Tweets<span class="follow">Follow</span></div>
    <div class="tweet"><span class="avatar"></span><div><div class="meta"><span>Fenrota <a>@Fenrota</a></span><time>3 May</time></div>Lorem ipsum dolor sit amet, consectetuer adipiscing elit, sed di nonummy nibh euismod tincidunt ut laoreet dolore ma</div></div>
    <div class="tweet"><span class="avatar"></span><div><div class="meta"><span>Fenrota <a>@Fenrota</a></span><time>3 May</time></div>Lorem ipsum dolor sit amet, consectetuer adipiscing elit, sed di nonummy nibh euismod tincidunt ut laoreet dolore ma</div></div>
  </div>
</footer>

<div class="bottombar">
  <span>© 2015 Fenrota . All Rights Reserved.</span>
  <div class="social"><i class="active"></i><i></i><i></i><i></i></div>
</div>
</body>
</html>
```